LUMEN PI Planning Web App - Lean Agile at Scale - Distributed Big Room Planning Web & Touchscr...

We are the provider of the boardweave app http://boardweave-demo.example which currently is a desktop application. We are now working to bring all the features to a web-app but we don’t have a catchy design yet. The boardweave app is a visual collaboration tool for globally distributed teams and organization. Imagine a wall with lots of sticky notes on a flipchart hanging there – that’s basically our app just in a digital format. In general we want a light, modern, state of the art look and feel. Please take colorblind people into consideration when designing it.We are specifically looking for the following two design parts:- Design of the board structure- Sticky note designRequirements for the board structure- 16:9 ratio fixed- The board can be structured in 2 to 12 iterations + Risk Area and Objectives. Most common is 5 iterations + Risk Area and Objectives. Please go with the most common one but have in the back of your head that it needs to be compatible with 14 sections. Just for your imagination: in real life each of these areas on the board is one flip chart page.- Team Name: Somewhere on the board has to be the team name. It has to be easy to find and read.- In the iteration fields the user can set a velocity. That’s a simple numbers field. The load is calculated automatically and is just a number displayed on the board. There is an automatic visual indicator which should show with green or red colors if the teams are still in the plan. How this is brought to the attention is up to you.- Objectives & Stretch Objectives: The area with the Objectives is a list with text and a prioritization number attached to it. BV on the sketch stands for Business Value.Sticky Note design descriptionThe Sticky Note represents a physical sticky note or post-it note. When the user sees it he should instantly understand it as a sticky note and so for intuitively know what to do with it.Unselected sticky noteIf the sticky note is not selected it should be a simple sticky note sitting on the board.Following you find the things visible when the sticky note is not selected:- The sticky notes have a squared form factor- There is the text which is on the sticky note- In the upper right corner is a small sticky ID. Something like e.g. RT-4253.- Somewhere on the sticky note is also a number which should be easy to read. The numbers range from nothing over 0.5, 1, 2, 3, 5, 8, 13, 20, 40 up to 100.- Somewhere on the sticky needs to be a permanent text label. Not bigger than the rest of the text on the sticky note but easy to read.Selected sticky noteIf the user clicks on the sticky note once the following information needs to be displayed and he needs to be able to do the things listed and described below:- The sticky notes have a squared form factor- The user can write text on it- He can select different colors. These colors need to have a label so he knows what the function of these colors are.- By clicking a button he can add a flag to the sticky note- He can open a selection to choose the following number displayed on the sticky: 0.5, 1, 2, 3, 5, 8, 13, 20, 40, 100.- There is a delete sticky button. Place it where it makes sense from an intuitive stand point.- If he clicks the delete button, a short dialog appears on the sticky note: “Are you sure you want to delete this sticky note permanently? (It might delete an issue in your ALM tool)” He can confirm that by pressing “Delete” or “Cancel”.- In the upper right corner is a small sticky ID. Something like e.g. RT-4253.- Somewhere on or next to the sticky note needs to be a “sticky mirror” button as well as a “sticky move” button. Beside an optional icon for “mirror” and “move” there needs to be a naming tag so that everyone understands it right away.- It’s up to you to decide what’s the most intuitive way for the user.For better understanding also take a look at the rough sketch attached.

Font styles to use
Sans Serif

Requirements
Must have
• Color blind mode for different colored sticky notes

```html
<!DOCTYPE html>
<html lang="en">
<head>
<meta charset="utf-8">
<title>Team Board – Iterations, Objectives and Sticky Notes</title>
<link href="https://fonts.googleapis.com/css2?family=Mulish:wght@300;400;600;700;800;900&display=swap" rel="stylesheet">
<style>
:root{
  --ink:#111;
  --muted:#9a9ca6;
  --line:#e3e5ee;
  --blue:#1a9be6;
  --red:#e8414e;
  --yellow:#f5c400;
  --purple:#5a1fa8;
  --default-dot:#e6e8f0;
  --iter3-bg:#f2f8fd;
  --iter5-bg:#fff3f3;
  --tab-blue:#dcecf9;
  --tab-pink:#f8d3d6;
  --tray:#eeeeee;
  --fold:#e2e5ee;
}
*{box-sizing:border-box;margin:0;padding:0}
html,body{width:1200px;height:938px;overflow:hidden;background:#fff}
body{font-family:'Mulish',sans-serif;color:var(--ink)}
.board{position:relative;width:1200px;height:938px;overflow:hidden}

/* header */
.board-header{position:absolute;left:0;top:0;width:1200px;height:60px;border-bottom:2px solid var(--line)}
.team-name{position:absolute;left:0;right:0;top:14px;text-align:center;font-weight:300;font-size:26px;letter-spacing:.3px}
.legend{position:absolute;left:1096px;top:11px;list-style:none}
.legend li{display:flex;align-items:center;font-size:8.5px;height:13.5px}
.legend .dot{width:8px;height:8px;border-radius:50%;margin-right:6px}
.dot-default{background:var(--default-dot)}
.dot-yellow{background:var(--yellow)}
.dot-purple{background:var(--purple)}

/* grid */
.section{position:absolute;border-right:2px solid var(--line);border-bottom:2px solid var(--line)}
.objectives{left:0;top:60px;width:210px;height:615px}
.col-a{left:210px;width:330px}
.col-b{left:540px;width:330px}
.col-c{left:870px;width:330px;border-right:none}
.row-1{top:60px;height:308px}
.row-2{top:368px;height:307px}
.tint-blue{background:var(--iter3-bg)}
.tint-pink{background:var(--iter5-bg)}
.tab{position:absolute;left:0;top:0;width:16px;height:24px;clip-path:polygon(0 0,100% 0,100% 100%,50% 82%,0 100%);display:flex;justify-content:center;padding-top:4px}
.tab-blue{background:var(--tab-blue)}
.tab-pink{background:var(--tab-pink)}

/* iteration header */
.iter-head{position:absolute;left:25px;top:22px;display:flex;align-items:baseline;white-space:nowrap}
.iter-title{font-weight:900;font-size:14.5px;letter-spacing:.2px;margin-right:12px}
.metric{font-size:8px;font-weight:600;margin-right:13px;display:inline-flex;align-items:baseline}
.metric-val{display:inline-block;width:24px;border-bottom:1px solid var(--ink);text-align:center;margin-left:3px;position:relative;top:-3px;font-size:8.5px;font-weight:400;line-height:10px}

/* objectives */
.obj-head{position:absolute;left:12px;top:20px;width:185px;display:flex;align-items:center;justify-content:space-between}
.obj-title{display:flex;align-items:center;color:var(--blue);font-weight:900;font-size:14px;letter-spacing:.2px}
.obj-title svg{margin-right:4px}
.bv{color:var(--blue);font-weight:900;font-size:12px}
.obj-list{position:absolute;left:12px;width:185px;list-style:none}
.obj-item{display:flex;justify-content:space-between;align-items:flex-start;border-bottom:1px solid var(--line);font-size:9.2px;line-height:13.6px}
.obj-item p{width:160px}
.obj-item b{font-weight:800;font-size:11px;line-height:13px}
.stretch-title{position:absolute;left:12px;top:188px;color:var(--blue);font-weight:900;font-size:12.5px;letter-spacing:.2px}

/* sticky note */
.note{position:absolute;width:90px;height:90px;background:#fff;border:1px solid #e4e6ec}
.note-fold{position:absolute;left:0;top:0;width:11px;height:11px;background:var(--fold);clip-path:polygon(100% 0,100% 100%,0 100%)}
.note-id{position:absolute;right:5px;top:4px;font-size:4.6px;font-weight:700;display:flex;align-items:center;gap:2px}
.note-cat{position:absolute;left:14px;top:4.5px;font-size:4px;color:var(--muted)}
.note-text{position:absolute;left:5px;right:5px;top:18px;font-size:5.7px;line-height:8.2px}
.note-label{position:absolute;left:5px;bottom:4px;font-size:4px;font-weight:600}
.note-points{position:absolute;right:5px;bottom:2px;font-size:9px;font-weight:300}
.note-yellow{border:1.5px solid var(--yellow)}
.note-yellow .note-fold{background:var(--yellow)}
.note-purple{border:1.5px solid var(--purple)}
.note-purple .note-fold{background:var(--purple)}
.note-risk{border:1px solid var(--red)}
.note-risk .note-fold{left:auto;right:0;background:var(--red);clip-path:polygon(0 0,100% 100%,0 100%)}
.note-risk .note-text{top:20px}

/* selected sticky */
.sticky{position:absolute;width:134px;height:158px;background:#fff;border:1px solid #1a1a1a;overflow:hidden}
.sticky-lift{box-shadow:0 3px 10px rgba(0,0,0,.18)}
.cat-select{position:absolute;left:6px;top:6px;width:96px;height:12px;border-bottom:1px solid var(--ink);display:flex;align-items:center;font-size:6px}
.cat-select .dot{width:6px;height:6px;border-radius:50%;background:var(--default-dot);margin-right:4px}
.cat-select svg{margin-left:auto;margin-right:3px}
.sticky-id{position:absolute;right:6px;top:6px;font-size:4.4px;color:#bfc1c8}
.sticky-text{position:absolute;left:6px;right:6px;top:27px;font-size:9px;line-height:12px}
.sticky-foot{position:absolute;left:6px;right:6px;top:118px;display:flex;align-items:flex-end}
.toggle{display:inline-flex;align-items:center;justify-content:space-between;width:18px;height:6px;border-radius:1.5px;background:var(--ink);margin-left:3px;padding:0 1px 0 3px;font-size:3px;font-weight:800;color:#fff}
.toggle i{width:4px;height:4px;background:#fff}
.sticky-points{margin-left:auto;font-size:14px;font-weight:300;line-height:14px}
.actions{position:absolute;left:0;right:0;bottom:0;height:24px;background:#000;display:flex}
.action{flex:1;display:flex;flex-direction:column;align-items:center;justify-content:center;color:#fff;font-size:3.9px;font-weight:800;letter-spacing:.2px;gap:2px}
.action + .action{border-left:1px solid #444}

/* dropdown */
.cat-menu{position:absolute;left:8px;top:19px;width:88px;background:#fff;box-shadow:0 2px 8px rgba(0,0,0,.15);padding:4px 0;list-style:none}
.cat-menu li{display:flex;align-items:center;font-size:5.6px;height:13.5px;padding-left:6px}
.cat-menu .dot{width:6px;height:6px;border-radius:50%;margin-right:4px}
.cat-menu .dot-new{border:0.8px solid var(--ink);background:#fff}

/* overlays */
.overlay{position:absolute;inset:0;background:rgba(28,28,28,.88);color:#fff}
.overlay-title{position:absolute;left:0;right:0;top:14px;text-align:center;font-weight:900;font-size:8px}
.field{position:absolute;left:7px;right:7px;top:33px;height:12px;border-bottom:1px solid #fff;font-size:6px;padding-left:2px}
.sv-area{position:absolute;left:9px;top:54px;width:65px;height:65px;background:linear-gradient(to top,#000,rgba(0,0,0,0)),linear-gradient(to right,#fff,#f8d905);outline:1px solid #555}
.sv-knob{position:absolute;right:-2px;top:-2px;width:4px;height:4px;border-radius:50%;border:0.8px solid #fff}
.hue{position:absolute;left:81px;top:54px;width:6px;height:65px;background:linear-gradient(to bottom,#f00,#ff0 18%,#0f0 34%,#0ff 50%,#00f 66%,#f0f 84%,#f00)}
.hue-knob{position:absolute;left:-1px;top:8px;width:8px;height:3px;border:0.8px solid #fff;border-radius:1px}
.swatch{position:absolute;left:94px;top:55px;width:32px;height:14px;border-radius:2px;background:#f8d905}
.rgb{position:absolute;left:98px;display:flex;align-items:center;font-size:4px;gap:3px}
.rgb span:last-child{display:block;width:22px;height:7px;background:#000;font-size:4px;line-height:7px;padding-left:3px}
.hex{position:absolute;left:94px;top:103px;width:32px;height:7px;background:#000;font-size:3.8px;line-height:7px;padding-left:3px}
.btn{position:absolute;height:13px;width:44px;display:flex;align-items:center;justify-content:center;gap:2px;font-size:4.6px;font-weight:800;border:1px solid #fff}
.btn-ghost{color:#fff;background:transparent}
.btn-solid{background:#fff;color:#000}
.confirm-text{position:absolute;left:6px;right:6px;top:60px;text-align:center;font-weight:800;font-size:7.3px;line-height:9.6px}

/* demo tray */
.tray{position:absolute;left:0;top:675px;width:1200px;height:263px;background:var(--tray)}
.demo{position:absolute;top:0}
.demo-caption{position:absolute;top:50px;width:134px;text-align:center;font-size:7px;color:#a7a9af;white-space:nowrap;font-weight:400}
.demo .sticky{top:67px}
</style>
</head>
<body>
<div class="board">

  <header class="board-header">
    <h1 class="team-name">Team Name</h1>
    <ul class="legend">
      <li><span class="dot dot-default"></span>Default Category</li>
      <li><span class="dot dot-yellow"></span>Color Category 1</li>
      <li><span class="dot dot-purple"></span>Color Category 2</li>
    </ul>
  </header>

  <!-- Objectives -->
  <section class="section objectives">
    <div class="obj-head">
      <span class="obj-title">
        <svg width="20" height="20" viewBox="0 0 20 20" fill="none" stroke="#1a9be6" stroke-width="1.6"><circle cx="9" cy="11" r="8"/><circle cx="9" cy="11" r="5"/><circle cx="9" cy="11" r="2"/><path d="M9 11 L17 3 M14 2 L17 3 L18 6"/></svg>
        OBJECTIVES
      </span>
      <span class="bv">BV</span>
    </div>
    <ul class="obj-list" style="top:56px">
      <li class="obj-item" style="padding-bottom:11px"><p>Lorem ipsum dolor sit amet, consectetur adipiscing elit. Nullamv diam non felis varius dignisim eget.</p><b>10</b></li>
      <li class="obj-item" style="padding:10px 0 12px"><p>Curabitur sagittis tortor at erat ultricies, ac hendrerit justo iaculis.</p><b>8</b></li>
    </ul>
    <h3 class="stretch-title">STRETCH OBJECTIVES</h3>
    <ul class="obj-list" style="top:212px">
      <li class="obj-item" style="padding-bottom:11px"><p>Pellentesque, dolor ac tristique pellentesque, diam tortor augue.</p><b>4</b></li>
      <li class="obj-item" style="padding:10px 0 11px"><p>Cras gravida scelerisque magna ultrices gregestas feugiat pharetra.</p><b>2</b></li>
    </ul>
  </section>

  <!-- Iteration 1 -->
  <section class="section col-a row-1">
    <div class="iter-head"><h2 class="iter-title">ITERATION 1</h2><span class="metric">Velocity<span class="metric-val">8</span></span><span class="metric">Load<span class="metric-val">6</span></span></div>
    <div class="note" style="left:214px;top:55px"><span class="note-fold"></span><span class="note-id">RT-4255</span><p class="note-text">Sed ullamcorper metus ut malesuada egestas. Erat, tellus vel vestibulum, eros ut massa vitae.</p><span class="note-label">Permanent Text Label</span><span class="note-points">13</span></div>
    <div class="note" style="left:25px;top:55px"><span class="note-fold"></span><span class="note-id">RT-4253</span><p class="note-text">Lorem ipsum dolor sit amet, consectetur adipiscing elit. Nullam vel diam non felis varius dignissim ege rabitur.</p><span class="note-label">Permanent Text Label</span><span class="note-points">20</span></div>
    <div class="note" style="left:25px;top:149px"><span class="note-fold"></span><span class="note-id">RT-4256</span><p class="note-text">Sed nec tincidunt velit, at consequat morbi vestibulum.</p><span class="note-label">Permanent Text Label</span><span class="note-points">8</span></div>

    <div class="sticky sticky-lift" style="left:120px;top:55px">
      <div class="cat-select"><span class="dot"></span>Default Category<svg width="6" height="4" viewBox="0 0 6 4"><path d="M.5.5 3 3 5.5.5" fill="none" stroke="#111" stroke-width=".8"/></svg></div>
      <span class="sticky-id">RT-4254</span>
      <p class="sticky-text">Cras gravida scelerisque magna ultrices gravida eget massa amet lectus justo.</p>
      <div class="sticky-foot"><svg width="6" height="7" viewBox="0 0 6 7"><path d="M.5 7V0h5L4.3 1.6 5.5 3.2H1.2" fill="#111"/></svg><span class="toggle">ON<i></i></span><span class="sticky-points">100</span></div>
      <div class="actions">
        <span class="action"><svg width="7" height="7" viewBox="0 0 7 7" fill="#fff"><rect x="2" y="0" width="5" height="5"/><rect x="0" y="2" width="5" height="5" stroke="#000" stroke-width=".6"/></svg>DUPLICATE</span>
        <span class="action"><svg width="8" height="8" viewBox="0 0 8 8" fill="#fff"><path d="M4 0 5.5 1.8H4.6V3.4H6.2V2.5L8 4 6.2 5.5V4.6H4.6V6.2H5.5L4 8 2.5 6.2H3.4V4.6H1.8V5.5L0 4 1.8 2.5V3.4H3.4V1.8H2.5Z"/></svg>MOVE</span>
        <span class="action"><svg width="6" height="7" viewBox="0 0 6 7" fill="#fff"><rect x="0" y="1" width="6" height="1"/><rect x="2" y="0" width="2" height="1"/><path d="M.6 2.4h4.8L5 7H1z"/></svg>DELETE</span>
      </div>
    </div>
  </section>

  <!-- Iteration 2 -->
  <section class="section col-b row-1">
    <div class="iter-head"><h2 class="iter-title">ITERATION 2</h2><span class="metric">Velocity<span class="metric-val">20</span></span><span class="metric">Load<span class="metric-val">10</span></span></div>
    <div class="note note-yellow" style="left:25px;top:55px"><span class="note-fold"></span><span class="note-cat">Color Category 1</span><span class="note-id"><svg width="4" height="5" viewBox="0 0 4 5"><path d="M.3 5V0h3.4L2.9 1.1l.8 1.1H.9" fill="#111"/></svg>RT-4257</span><p class="note-text">In in augue id pellentesque condimentum in quis nulla fermentum sapien metus.</p><span class="note-label">Permanent Text Label</span><span class="note-points">0.5</span></div>
    <div class="note note-purple" style="left:119px;top:55px"><span class="note-fold"></span><span class="note-cat">Color Category 2</span><span class="note-id">RT-4258</span><p class="note-text">Phasellus eu tempor mauris. Etiam at ipsum nec libero imperdiet pharetra raesent finibus ante enim dictum.</p><span class="note-label">Permanent Text Label</span><span class="note-points">2</span></div>
  </section>

  <!-- Iteration 3 -->
  <section class="section col-c row-1 tint-blue">
    <span class="tab tab-blue"><svg width="9" height="9" viewBox="0 0 10 10" fill="#fff"><path d="M4.2 0h1.6l.3 1.5 1.2.6 1.3-.9 1.1 1.1-.9 1.3.6 1.2 1.5.3v1.6l-1.5.3-.6 1.2.9 1.3-1.1 1.1-1.3-.9-1.2.6-.3 1.5H4.2l-.3-1.5-1.2-.6-1.3.9L.3 8.6l.9-1.3-.6-1.2L0 5.8V4.2l1.5-.3.6-1.2-.9-1.3L2.3.3l1.3.9 1.2-.6zM5 3.3A1.7 1.7 0 1 0 5 6.7 1.7 1.7 0 0 0 5 3.3z"/></svg></span>
    <div class="iter-head"><h2 class="iter-title">ITERATION 3</h2><span class="metric">Velocity<span class="metric-val">13</span></span><span class="metric">Load<span class="metric-val">2</span></span></div>
    <div class="note" style="left:25px;top:55px"><span class="note-fold"></span><span class="note-id">RT-4259</span><p class="note-text">Mauris sodales diam ultricis sollicitudin dictum finibus.</p><span class="note-label">Permanent Text Label</span><span class="note-points">40</span></div>
  </section>

  <!-- Iteration 4 -->
  <section class="section col-a row-2">
    <div class="iter-head"><h2 class="iter-title">ITERATION 4</h2><span class="metric">Velocity<span class="metric-val">&nbsp;</span></span></div>
  </section>

  <!-- Iteration 5 -->
  <section class="section col-b row-2 tint-pink">
    <span class="tab tab-pink"><svg width="10" height="7" viewBox="0 0 10 7" fill="none" stroke="#fff" stroke-width="1.1"><path d="M.6 3.5C2 1.3 3.4.6 5 .6S8 1.3 9.4 3.5C8 5.7 6.6 6.4 5 6.4S2 5.7.6 3.5z"/><circle cx="5" cy="3.5" r="1.3"/></svg></span>
    <div class="iter-head"><h2 class="iter-title">ITERATION 5</h2><span class="metric">Velocity<span class="metric-val">5</span></span><span class="metric">Load<span class="metric-val">13</span></span></div>
    <div class="note" style="left:25px;top:55px"><span class="note-fold"></span><span class="note-id">RT-4260</span><p class="note-text">Aliquam dignissim ante sit amet consectetur vehicula. Vestibulum erat mauris, placerat tempor imperdiet.</p><span class="note-label">Permanent Text Label</span><span class="note-points">3</span></div>
    <div class="note" style="left:119px;top:55px"><span class="note-fold"></span><span class="note-id">RT-4261</span><p class="note-text">Curabitur vitae lacinia finibus nunc amet egestas.</p><span class="note-label">Permanent Text Label</span><span class="note-points">1</span></div>
    <div class="note" style="left:214px;top:55px"><span class="note-fold"></span><span class="note-id">RT-4262</span><p class="note-text">Donec pretium nibh vitae dolor vulputate pretium. uspendisse et purus pharetra, convallis quam vestibulum, aliquam lorem.</p><span class="note-label">Permanent Text Label</span><span class="note-points">0.5</span></div>
  </section>

  <!-- Risks -->
  <section class="section col-c row-2">
    <div class="iter-head" style="align-items:center">
      <svg width="21" height="18" viewBox="0 0 21 18" fill="none" stroke="#e8414e" stroke-width="1.2" style="margin-right:3px"><path d="M10.5 1 20 17H1z"/><path d="M10.5 6.5v5.5M10.5 13.5v1.5" stroke-width="1.5"/></svg>
      <h2 class="iter-title" style="color:var(--red)">RISKS</h2>
    </div>
    <div class="note note-risk" style="left:25px;top:55px"><span class="note-fold"></span><p class="note-text">Integer enim enim, efficitur a est pharetra lacinia mass fusce dictum velit gravida.</p></div>
    <div class="note note-risk" style="left:119px;top:55px"><span class="note-fold"></span><p class="note-text">Suspendisse et purus pharet convallis vestibulum, aliqua lorem. Nullam auctor tortor blandit leo mattis blandit estibulum ante ipsum primis.</p></div>
  </section>

  <!-- Sticky note states -->
  <section class="tray">

    <div class="demo" style="left:271px">
      <p class="demo-caption">Selected sticky note</p>
      <div class="sticky">
        <div class="cat-select"><span class="dot"></span>Default Category<svg width="6" height="4" viewBox="0 0 6 4"><path d="M.5.5 3 3 5.5.5" fill="none" stroke="#111" stroke-width=".8"/></svg></div>
        <span class="sticky-id">RT-4254</span>
        <p class="sticky-text">Cras gravida scelerisque magna ultrices gravida eget massa amet lectus justo.</p>
        <div class="sticky-foot"><svg width="6" height="7" viewBox="0 0 6 7"><path d="M.5 7V0h5L4.3 1.6 5.5 3.2H1.2" fill="#111"/></svg><span class="toggle">ON<i></i></span><span class="sticky-points">100</span></div>
        <div class="actions">
          <span class="action"><svg width="7" height="7" viewBox="0 0 7 7" fill="#fff"><rect x="2" y="0" width="5" height="5"/><rect x="0" y="2" width="5" height="5" stroke="#000" stroke-width=".6"/></svg>DUPLICATE</span>
          <span class="action"><svg width="8" height="8" viewBox="0 0 8 8" fill="#fff"><path d="M4 0 5.5 1.8H4.6V3.4H6.2V2.5L8 4 6.2 5.5V4.6H4.6V6.2H5.5L4 8 2.5 6.2H3.4V4.6H1.8V5.5L0 4 1.8 2.5V3.4H3.4V1.8H2.5Z"/></svg>MOVE</span>
          <span class="action"><svg width="6" height="7" viewBox="0 0 6 7" fill="#fff"><rect x="0" y="1" width="6" height="1"/><rect x="2" y="0" width="2" height="1"/><path d="M.6 2.4h4.8L5 7H1z"/></svg>DELETE</span>
        </div>
      </div>
    </div>

    <div class="demo" style="left:424px">
      <p class="demo-caption">Select a category/color.</p>
      <div class="sticky">
        <div class="cat-select"><span class="dot"></span>Default Category<svg width="6" height="4" viewBox="0 0 6 4"><path d="M.5.5 3 3 5.5.5" fill="none" stroke="#111" stroke-width=".8"/></svg></div>
        <span class="sticky-id">RT-4254</span>
        <p class="sticky-text">Cras gravida scelerisque magna ultrices gravida eget massa amet lectus justo.</p>
        <div class="sticky-foot"><svg width="6" height="7" viewBox="0 0 6 7"><path d="M.5 7V0h5L4.3 1.6 5.5 3.2H1.2" fill="#111"/></svg><span class="toggle">ON<i></i></span><span class="sticky-points">100</span></div>
        <div class="actions">
          <span class="action"><svg width="7" height="7" viewBox="0 0 7 7" fill="#fff"><rect x="2" y="0" width="5" height="5"/><rect x="0" y="2" width="5" height="5" stroke="#000" stroke-width=".6"/></svg>DUPLICATE</span>
          <span class="action"><svg width="8" height="8" viewBox="0 0 8 8" fill="#fff"><path d="M4 0 5.5 1.8H4.6V3.4H6.2V2.5L8 4 6.2 5.5V4.6H4.6V6.2H5.5L4 8 2.5 6.2H3.4V4.6H1.8V5.5L0 4 1.8 2.5V3.4H3.4V1.8H2.5Z"/></svg>MOVE</span>
          <span class="action"><svg width="6" height="7" viewBox="0 0 6 7" fill="#fff"><rect x="0" y="1" width="6" height="1"/><rect x="2" y="0" width="2" height="1"/><path d="M.6 2.4h4.8L5 7H1z"/></svg>DELETE</span>
        </div>
        <ul class="cat-menu">
          <li><span class="dot dot-default"></span>Default Category</li>
          <li><span class="dot dot-yellow"></span>Color Category 1</li>
          <li><span class="dot dot-purple"></span>Color Category 2</li>
          <li><span class="dot dot-new"></span>Create a New Category</li>
        </ul>
      </div>
    </div>

    <div class="demo" style="left:577px">
      <p class="demo-caption">Create a new category</p>
      <div class="sticky">
        <div class="cat-select"><span class="dot"></span>Default Category</div>
        <p class="sticky-text">Cras gravida scelerisque magna ultrices gravida eget massa amet lectus justo.</p>
        <div class="sticky-foot"><span class="sticky-points">100</span></div>
        <div class="actions"><span class="action">DUPLICATE</span><span class="action">MOVE</span><span class="action">DELETE</span></div>
        <div class="overlay">
          <p class="overlay-title">CREATE A CATEGORY</p>
          <div class="field">Category Name</div>
          <div class="sv-area"><span class="sv-knob"></span></div>
          <div class="hue"><span class="hue-knob"></span></div>
          <div class="swatch"></div>
          <div class="rgb" style="top:77px;left:99px"><span>R</span><span>248</span></div>
          <div class="rgb" style="top:87px;left:99px"><span>G</span><span>217</span></div>
          <div class="rgb" style="top:98px;left:99px"><span>B</span><span>5</span></div>
          <div class="hex" style="top:111px">#f8d905</div>
          <span class="btn btn-ghost" style="left:21px;top:132px">CANCEL</span>
          <span class="btn btn-solid" style="left:69px;top:132px"><svg width="5" height="5" viewBox="0 0 5 5" fill="#000"><rect width="2" height="2"/><rect x="3" width="2" height="2"/><rect y="3" width="2" height="2"/><rect x="3" y="3" width="2" height="2"/></svg>CREATE</span>
        </div>
      </div>
    </div>

    <div class="demo" style="left:787px">
      <p class="demo-caption">Delete the sticky note</p>
      <div class="sticky">
        <div class="cat-select"><span class="dot"></span>Default Category</div>
        <p class="sticky-text">Cras gravida scelerisque magna ultrices gravida eget massa amet lectus justo.</p>
        <div class="sticky-foot"><span class="sticky-points">100</span></div>
        <div class="actions"><span class="action">DUPLICATE</span><span class="action">MOVE</span><span class="action">DELETE</span></div>
        <div class="overlay">
          <p class="confirm-text">Are you sure you want to delete this sticky note permanently?</p>
          <span class="btn btn-ghost" style="left:21px;top:84px">CANCEL</span>
          <span class="btn btn-solid" style="left:69px;top:84px"><svg width="4" height="5" viewBox="0 0 6 7" fill="#000"><rect x="0" y="1" width="6" height="1"/><rect x="2" y="0" width="2" height="1"/><path d="M.6 2.4h4.8L5 7H1z"/></svg>DELETE</span>
        </div>
      </div>
    </div>

  </section>
</div>
</body>
</html>
```